PowerPoint Design Project for Veltro Bonding AB - a innovative adhesives company

We are looking to lift our current sales PPT template to convey a professional maturer image. Veltro Bonding AB (www.veltrobonding.example) develop a unique switchable adhesive that can be used in many different industries. Our strength in our technology is that the adhesive is stronger yet easier to remove in the same product.
We want to maintain our logo including its font (see attached).
We want to convey innovation, trustworthiness, Nordic (Sweden based) and high end (high tech) products.
Target Market(s)
Product managers, technical product owners, upper management, higher education levels.
Industry/Entity Type
It Company
Requirements
Must have
- 1) Existing logo
2) Index for presentation
3) Page numbers - or cool progress indicator indicating how much is left of the presentation
4) End slide - including contact details
5) Indicator of confidentiality
6) Headers, sub-headers, bullets synced (style)
Should not have
- Sounds and animations

```html
<!DOCTYPE html>
<html lang="en">
<head>
<meta charset="utf-8">
<title>About Veltro</title>
<link rel="stylesheet" href="https://fonts.googleapis.com/css2?family=Titillium+Web:wght@300;400&family=Open+Sans:wght@400;600&family=Oswald:wght@500&display=swap">
<style>
  :root {
    --brand-blue: #1a9ad6;
    --ink-dark: #333638;
    --ink-body: #555759;
    --header-top: #ffffff;
    --header-bottom: #e6e6e7;
    --footer-band: #555a5c;
    --footer-line: #2a9fd8;
    --divider: #d9dadb;
    --texture: #ededee;
    --page: #ffffff;
  }
  * { margin: 0; padding: 0; box-sizing: border-box; }
  html, body { width: 1200px; height: 900px; overflow: hidden; background: var(--page); }
  .slide { position: relative; width: 1200px; height: 900px; background: var(--page); overflow: hidden; }

  .slide-header {
    position: absolute; left: 0; top: 0; width: 1200px; height: 100px;
    background: linear-gradient(to bottom, var(--header-top), var(--header-bottom));
  }
  .slide-title {
    position: absolute; left: 39px; top: 22px;
    font: 300 40px/1 "Titillium Web", sans-serif; color: var(--ink-dark);
  }
  .accent { color: var(--brand-blue); }

  .brand-mark {
    position: absolute; right: 34px; top: 28px;
    display: flex; align-items: center; gap: 12px;
  }
  .brand-name {
    font: 400 34px/1 "Titillium Web", sans-serif; color: var(--ink-dark); letter-spacing: 2px;
  }
  .brand-dot { width: 30px; height: 30px; border-radius: 50%; background: var(--brand-blue); }

  .texture-area {
    position: absolute; left: 600px; top: 100px; width: 600px; height: 650px;
    background: radial-gradient(ellipse at 100% 20%, var(--texture) 0%, rgba(237,237,238,0.6) 35%, rgba(255,255,255,0) 75%);
  }

  .column-divider {
    position: absolute; left: 598px; top: 165px; width: 2px; height: 590px;
    background: linear-gradient(to bottom, rgba(217,218,219,0), var(--divider) 20%, var(--divider) 70%, rgba(217,218,219,0));
  }

  .content-column { position: absolute; top: 166px; width: 481px; }
  .content-column.left { left: 70px; }
  .content-column.right { left: 640px; }
  .content-title {
    font: 400 35px/1.2 "Titillium Web", sans-serif; color: var(--ink-dark); margin-bottom: 18px;
  }
  .content-text {
    font: 400 20.5px/39px "Open Sans", sans-serif; color: var(--ink-body);
    text-align: justify; margin-bottom: 39px;
  }
  .content-text strong { font-weight: 600; color: var(--ink-dark); }

  .footer-line { position: absolute; left: 0; top: 844px; width: 1200px; height: 7px; background: var(--footer-line); }
  .slide-footer { position: absolute; left: 0; top: 851px; width: 1200px; height: 49px; background: var(--footer-band); }
  .copyright {
    position: absolute; right: 52px; top: 10px;
    font: 500 21px/1.2 "Oswald", sans-serif; color: #ffffff; letter-spacing: 0.5px;
  }
</style>
</head>
<body>
<main class="slide">
  <header class="slide-header">
    <h1 class="slide-title">About <span class="accent">Veltro</span></h1>
    <div class="brand-mark">
      <span class="brand-name">VELTRO BONDING</span>
      <span class="brand-dot"></span>
    </div>
  </header>

  <div class="texture-area" role="img" aria-label="Soft grey dotted background texture"></div>
  <div class="column-divider"></div>

  <section class="content-column left">
    <h2 class="content-title">Content <span class="accent">Title Here</span></h2>
    <p class="content-text"><strong>Lorem ipsum dolor sit ipsum</strong> Lorem ipsum dolor sit ipsum Lorem ipsum Lorem ipsum dolor sit ipsum Lorem ipsum dolor sit ipsum Lorem ipsum.</p>
    <p class="content-text"><strong>Lorem ipsum dolor sit</strong> ipsum Lorem ipsum dolor sit ipsum Lorem ipsum Lorem ipsum dolor sit ipsum Lorem ipsum dolor sit ipsum Lorem ipsum.</p>
    <p class="content-text">Lorem ipsum dolor sit ipsum Lorem ipsum dolor sit ipsum Lorem ipsum Lorem ipsum dolor sit ipsum Lorem ipsum dolor sit ipsum Lorem ipsum.</p>
  </section>

  <section class="content-column right">
    <h2 class="content-title">Content <span class="accent">Title Here</span></h2>
    <p class="content-text">Lorem ipsum dolor sit ipsum Lorem ipsum dolor sit ipsum Lorem ipsum Lorem ipsum dolor sit ipsum Lorem ipsum dolor sit ipsum Lorem ipsum.</p>
    <p class="content-text">Lorem ipsum dolor sit ipsum Lorem ipsum dolor sit ipsum Lorem ipsum Lorem ipsum dolor sit ipsum Lorem ipsum dolor sit ipsum Lorem ipsum.</p>
    <p class="content-text">Lorem ipsum dolor sit ipsum Lorem ipsum dolor sit ipsum Lorem ipsum Lorem ipsum dolor sit ipsum Lorem ipsum dolor sit ipsum Lorem ipsum.</p>
  </section>

  <div class="footer-line"></div>
  <footer class="slide-footer">
    <span class="copyright">Copyright@2013</span>
  </footer>
</main>
</body>
</html>
```